Flier redesign 2021

The 3 prior year fliers are attached. We want a new design for 2021 -

* DO NOT SIMPLY COPY and change the year.
*All text should be the same, except year is 2021.
*Use different photos. You can find photos on our website maplecrestgardens.org or on our google page.

Requirements
Must have
• MUST be done in photoshop an photoshop file must be provided at the end.
Should not have
• Should not be same design as previous years.

```html
<!DOCTYPE html>
<html lang="en">
<head>
<meta charset="utf-8">
<title>2021 Landscape Packages — Maplecrest Gardens</title>
<link rel="stylesheet" href="https://fonts.googleapis.com/css2?family=Raleway:wght@400&family=Prata&family=Domine:wght@400;700&display=swap">
<style>
  :root {
    --page: #ffffff;
    --gold: #b8932f;
    --gold-dark: #9c7a22;
    --cream: #f4eee2;
    --card: rgba(242, 228, 200, 0.9);
    --red: #8e1c1f;
    --ink: #2a2320;
    --rule: rgba(120, 95, 60, 0.35);
    --white: #ffffff;
  }
  * { box-sizing: border-box; margin: 0; padding: 0; }
  html, body { width: 1200px; height: 1200px; overflow: hidden; background: var(--page); }
  .flier {
    position: absolute; left: 175px; top: 47px;
    width: 850px; height: 1106px; overflow: hidden;
    background: linear-gradient(160deg, var(--gold) 0%, #c19d3a 50%, var(--gold-dark) 100%);
    font-family: "Domine", Georgia, serif; color: var(--ink);
  }
  .brand {
    position: absolute; left: 24px; top: 22px; width: 90px; height: 90px;
    border-radius: 50%; background: var(--white);
    display: flex; align-items: center; justify-content: center; text-align: center;
    font-family: "Prata", Georgia, serif; color: var(--red); font-size: 13px; line-height: 1.1;
  }
  .title-rule { position: absolute; left: 128px; width: 700px; height: 1px; background: rgba(255,255,255,0.75); }
  .title-rule.top { top: 46px; }
  .title-rule.bottom { top: 104px; }
  .title {
    position: absolute; left: 166px; top: 50px; width: 660px;
    font-family: "Raleway", Arial, sans-serif; font-weight: 400; font-size: 40px; line-height: 50px;
    letter-spacing: 1px; color: var(--white); white-space: nowrap;
  }
  .package {
    position: absolute; top: 149px; width: 257px; height: 780px;
    border-radius: 22px; background: var(--card);
    padding: 22px 14px 0; text-align: center;
  }
  .package.perpetual { left: 20px; background: var(--cream); }
  .package.seasonal { left: 297px; }
  .package.basic { left: 577px; }
  .package-name {
    font-family: "Prata", Georgia, serif; font-weight: 400; color: var(--red);
    font-size: 19px; line-height: 1.2; min-height: 46px;
  }
  .seasonal .package-name { padding-top: 12px; }
  .package-lead { font-weight: 700; font-size: 13px; line-height: 1.3; margin: 16px 4px 20px; }
  .features { list-style: none; font-size: 12.5px; line-height: 1.32; }
  .features li { padding: 5px 0; border-bottom: 1px solid var(--rule); }
  .features li:last-child { border-bottom: none; }
  .terms { display: flex; justify-content: space-around; font-size: 12.5px; margin-top: 22px; }
  .term { display: flex; flex-direction: column; align-items: center; gap: 10px; }
  .price { font-family: "Prata", Georgia, serif; color: var(--red); }
  .term .price { font-size: 26px; }
  .price-block { margin-top: 22px; font-size: 12.5px; line-height: 1.35; }
  .perpetual .price-block { margin-top: 36px; }
  .price-block .price { display: block; font-size: 40px; line-height: 1.25; }
  .note { font-size: 12.5px; line-height: 1.35; margin-top: 16px; }
  .badge {
    position: absolute; left: 248px; top: 196px; width: 50px; height: 50px; border-radius: 50%;
    background: var(--red); color: var(--white); font-size: 6px; line-height: 1.15;
    display: flex; align-items: center; justify-content: center; text-align: center;
    text-transform: uppercase; transform: rotate(-20deg); font-weight: 700; z-index: 3;
  }
  .scene { position: absolute; left: 0; top: 0; width: 850px; height: 1106px; z-index: 1; }
  .contact-band {
    position: absolute; left: 0; top: 1044px; width: 850px; height: 40px; z-index: 2;
    background: var(--red); color: var(--white);
    display: flex; justify-content: space-around; align-items: center;
    font-size: 15px;
  }
</style>
</head>
<body>
<main class="flier">
  <div class="brand">Maplecrest<br>Gardens</div>
  <div class="title-rule top"></div>
  <h1 class="title">2021 LANDSCAPE PACKAGES</h1>
  <div class="title-rule bottom"></div>

  <section class="package perpetual">
    <h2 class="package-name">PERPETUAL CARE ENDOWMENT</h2>
    <p class="package-lead">Landscaping care forever for graves with plantings.</p>
    <ul class="features">
      <li>Weeding and trimming services on your gravesite approximately every 7 weeks during the growing season: mid-April through mid-October</li>
      <li>Monument leveling and cleaning</li>
      <li>Payment ensures grave care forever</li>
      <li>Full bed of boxwood shrubs</li>
      <li>Replacement of shrubs</li>
      <li>Trust certificate</li>
    </ul>
    <div class="price-block">12 Monthly Payments of<span class="price">$313</span>Call for single payment discount.<br>Valid through 10/31/2021</div>
  </section>
  <div class="badge">Most<br>Popular<br>Package</div>

  <section class="package seasonal">
    <h2 class="package-name">SEASONAL CARE</h2>
    <p class="package-lead">Seasonal landscaping<br>grave care.</p>
    <ul class="features">
      <li>Weeding and trimming services on your gravesite approximately every 7 weeks during the growing Season: mid-April through mid-October</li>
    </ul>
    <div class="terms">
      <div class="term">3 Years<span class="price">$357</span></div>
      <div class="term">2 Years<span class="price">$238</span></div>
      <div class="term">1 Years<span class="price">$119</span></div>
    </div>
    <p class="note">Multi-year payment locks<br>in current rates.<br>Valid through 10/31/2021</p>
  </section>

  <section class="package basic">
    <h2 class="package-name">BASIC CARE ENDOWMENT</h2>
    <p class="package-lead">Landscaping care forever for graves with no plantings.</p>
    <ul class="features">
      <li>Weeding and trimming services on your gravesite 2 times per year: mid-May and mid-September</li>
      <li>Monument leveling</li>
      <li>Payment ensures grave care forever</li>
    </ul>
    <div class="price-block">12 Monthly Payments of<span class="price">$255</span>Call for single payment discount.<br>Valid through 10/31/2021</div>
  </section>

  <svg class="scene" viewBox="0 0 850 1106" role="img" aria-label="Photo of cemetery grounds with headstones under autumn trees at sunset">
    <defs>
      <linearGradient id="sceneTone" x1="0" y1="0" x2="0" y2="1">
        <stop offset="0" stop-color="#8a6a3a"/>
        <stop offset="0.35" stop-color="#5a4a35"/>
        <stop offset="0.7" stop-color="#4a4a45"/>
        <stop offset="1" stop-color="#3a3328"/>
      </linearGradient>
      <radialGradient id="sunGlow" cx="0.87" cy="0.1" r="0.3">
        <stop offset="0" stop-color="#f5d59a" stop-opacity="0.9"/>
        <stop offset="1" stop-color="#f5d59a" stop-opacity="0"/>
      </radialGradient>
    </defs>
    <path d="M0 900 Q 340 640 850 600 L850 1106 L0 1106 Z" fill="url(#sceneTone)"/>
    <path d="M0 900 Q 340 640 850 600 L850 1106 L0 1106 Z" fill="url(#sunGlow)"/>
  </svg>

  <footer class="contact-band">
    <span>(201) 555-0148</span>
    <span>48 Elm Row, Fairhaven NJ 07410</span>
    <span>maplecrestgardens.org</span>
  </footer>
</main>
</body>
</html>
```